Custom Business Card Design

We are looking for a raised spot logo design to use with Tavu.com. We will provide the logo files. Should be a front and back design. We want to implement the house into the back design using the same colors as the logo through out. Something VERY cool!

```html
<!DOCTYPE html>
<html lang="en">
<head>
<meta charset="utf-8">
<title>Brightkey Homes Business Card</title>
<link href="https://fonts.googleapis.com/css2?family=Montserrat:wght@400;500;600&family=Oswald:wght@500&display=swap" rel="stylesheet">
<style>
  :root {
    --backdrop: #1b1b1b;
    --card: #262626;
    --card-edge: #2e2e2e;
    --blue: #3a7fd0;
    --red: #d23b3b;
    --silver: #b8b8b8;
    --text: #e6e6e6;
  }
  * { margin: 0; padding: 0; box-sizing: border-box; }
  html, body { width: 1200px; height: 900px; overflow: hidden; }
  body {
    background: radial-gradient(ellipse at 60% 40%, #2a2a2a 0%, var(--backdrop) 70%);
    font-family: "Montserrat", sans-serif;
    color: var(--text);
    position: relative;
  }
  .card {
    position: absolute;
    left: 285px;
    width: 630px;
    height: 360px;
    background: linear-gradient(135deg, var(--card) 0%, var(--card-edge) 100%);
    box-shadow: 0 12px 30px rgba(0,0,0,.55);
    overflow: hidden;
  }
  .card::after {
    content: "";
    position: absolute;
    left: 0; right: 0; bottom: 0;
    height: 7px;
    background: var(--blue);
  }
  .card-front { top: 60px; }
  .card-back { top: 470px; }

  .brand {
    position: absolute;
    top: 120px;
    left: 0; right: 0;
    display: flex;
    align-items: center;
    justify-content: center;
    gap: 14px;
  }
  .brand-mark {
    width: 18px; height: 18px;
    background: var(--silver);
  }
  .brand-name {
    font-weight: 600;
    font-size: 40px;
    color: var(--silver);
    letter-spacing: 1px;
  }
  .front-web {
    position: absolute;
    bottom: 40px;
    left: 0; right: 0;
    text-align: center;
    font-size: 14px;
    letter-spacing: 2px;
  }

  .identity {
    position: absolute;
    top: 118px;
    right: 340px;
    text-align: right;
  }
  .person-name {
    font-family: "Oswald", sans-serif;
    font-weight: 500;
    font-size: 36px;
    color: var(--blue);
    text-transform: uppercase;
    line-height: 1.1;
  }
  .person-role { font-size: 17px; margin-top: 2px; }
  .divider {
    position: absolute;
    top: 112px;
    left: 308px;
    width: 2px;
    height: 80px;
    background: var(--red);
  }
  .contacts {
    position: absolute;
    top: 118px;
    left: 330px;
    list-style: none;
    font-size: 15px;
    letter-spacing: .6px;
  }
  .contacts li {
    display: flex;
    align-items: center;
    gap: 12px;
    height: 24px;
  }
  .contacts svg { width: 14px; height: 14px; flex: none; }
  .location {
    position: absolute;
    bottom: 40px;
    left: 60px;
    font-size: 15px;
    letter-spacing: .8px;
  }
  .location-label { color: var(--blue); font-weight: 500; }
</style>
</head>
<body>
  <section class="card card-front">
    <div class="brand">
      <span class="brand-mark"></span>
      <span class="brand-name">Brightkey Homes</span>
    </div>
    <p class="front-web">www.brightkeyhomes.com</p>
  </section>

  <section class="card card-back">
    <div class="identity">
      <h1 class="person-name">Daniel Brooks</h1>
      <p class="person-role">Founder</p>
    </div>
    <span class="divider"></span>
    <ul class="contacts">
      <li>
        <svg viewBox="0 0 14 14" aria-hidden="true"><rect x="4" y="1" width="6" height="12" rx="1" fill="none" stroke="var(--blue)" stroke-width="1.4"/></svg>
        0400 555 019
      </li>
      <li>
        <svg viewBox="0 0 14 14" aria-hidden="true"><rect x="1" y="3" width="12" height="8" fill="var(--blue)"/><path d="M1 3 L7 8 L13 3" fill="none" stroke="var(--card)" stroke-width="1.2"/></svg>
        info@brightkeyhomes.com
      </li>
      <li>
        <svg viewBox="0 0 14 14" aria-hidden="true"><circle cx="6" cy="6" r="4" fill="none" stroke="var(--blue)" stroke-width="1.8"/><line x1="9" y1="9" x2="13" y2="13" stroke="var(--blue)" stroke-width="2"/></svg>
        www.brightkeyhomes.com
      </li>
    </ul>
    <p class="location"><span class="location-label">Location:</span> 2210 Alder Lane mailing Springfield, USA</p>
  </section>
</body>
</html>
```